Willowmere Counseling (Endure - Mend - Flourish) - Double Sided Business Card

I would like a 2-sided business card. Front: Matte Black or Navy with Logo & Tagline. Back: Name, Address, Phone Number, Email, & Website (maybe would like to include a small map pin-pointing location); Prefer front to be a gold/silver foil (iridescent); Back prefer white or light colored background with lettering that is easy to read and simple

Target Market(s)

Individuals & Couples (13 y.o. - ALL Adults); High end clientele

Industry/Entity Type

Licensed Professional Counselor (Mental Health)

Contact Information for Business Card

Name: Willowmere Counseling; Tagline: Endure - Mend - Flourish; Address: 3870 N. Garrick Ave., Suite 214, Fort Worth, TX 76132; Phone: (214) 555-0187; Website: www.WillowmereCounseling.example

Font styles to use
Serif

Requirements
Must have
• Logo on Front (Large) prefer gold/silver foil on a matte dark color (i.e. black, navy, etc.); Back of Card: All other relevant information

```html
<!DOCTYPE html>
<html lang="en">
<head>
<meta charset="utf-8">
<title>Willowmere Counseling – Business Card</title>
<link rel="stylesheet" href="https://fonts.googleapis.com/css2?family=Cinzel:wght@400;600&family=Poppins:wght@400;600&family=Tinos&display=swap">
<style>
  :root {
    --ink: #111111;
    --ink-soft: #1c1c1c;
    --gold: #d4b558;
    --silver: #8e8f91;
    --paper: #ffffff;
    --text-dark: #2a2a2a;
    --canvas: #ffffff;
  }
  * { box-sizing: border-box; margin: 0; padding: 0; }
  html, body { width: 749px; height: 1200px; overflow: hidden; background: var(--canvas); }
  .sheet { position: relative; width: 749px; height: 1200px; }
  .card {
    position: absolute; left: 74px; width: 600px; height: 341px; overflow: hidden;
    box-shadow: 3px 4px 6px rgba(0,0,0,0.35);
  }
  .card--front { top: 240px; background: linear-gradient(135deg, var(--ink-soft), var(--ink)); }
  .card--back { top: 615px; background: var(--ink); }

  /* front */
  .front-mark { position: absolute; left: 258px; top: 58px; width: 84px; height: 84px; border-radius: 50%; border: 3px solid var(--gold); }
  .front-name {
    position: absolute; left: 0; right: 0; top: 160px; text-align: center;
    font-family: "Cinzel", serif; font-weight: 600; font-size: 31px; color: var(--gold); letter-spacing: 0.5px;
  }
  .front-rule { position: absolute; top: 209px; left: 157px; width: 286px; height: 2px; background: var(--silver); }
  .front-tagline {
    position: absolute; left: 0; right: 0; top: 220px; text-align: center;
    font-family: "Cinzel", serif; font-size: 15px; color: var(--gold); letter-spacing: 0.5px;
  }
  .front-dots { position: absolute; left: 0; right: 0; top: 283px; display: flex; justify-content: center; align-items: center; gap: 7px; }
  .front-dots span { width: 4px; height: 4px; border-radius: 50%; background: var(--silver); }
  .front-dots span.is-main { width: 7px; height: 7px; background: var(--gold); }
  .front-web {
    position: absolute; left: 0; right: 0; top: 298px; text-align: center;
    font-family: "Poppins", sans-serif; font-size: 11px; letter-spacing: 2.4px; color: var(--silver);
  }
  .front-web b { color: var(--gold); font-weight: 600; }

  /* back */
  .back-panel { position: absolute; inset: 0; }
  .back-mark-row { position: absolute; left: 30px; top: 128px; width: 160px; text-align: center; }
  .back-mark { width: 44px; height: 44px; border-radius: 50%; border: 2px solid var(--gold); margin: 0 auto 8px; }
  .back-name { font-family: "Cinzel", serif; font-weight: 600; font-size: 13px; color: var(--gold); line-height: 1.15; }
  .back-tagline { font-family: "Cinzel", serif; font-size: 7px; color: var(--gold); margin-top: 4px; letter-spacing: 0.3px; }

  .info { position: absolute; left: 328px; top: 81px; width: 240px; }
  .info-pill {
    display: inline-block; background: var(--gold); color: var(--paper); border-radius: 14px;
    font-family: "Tinos", serif; font-size: 13.5px; padding: 5px 11px; letter-spacing: 0.3px;
  }
  .info-tagline { font-family: "Tinos", serif; font-size: 11px; color: var(--text-dark); margin: 8px 0 0 2px; letter-spacing: 0.3px; }
  .info-list { list-style: none; margin-top: 22px; position: relative; }
  .info-list::before {
    content: ""; position: absolute; left: 12px; top: 18px; bottom: 18px;
    border-left: 1px dotted var(--gold);
  }
  .info-item { position: relative; display: flex; align-items: center; gap: 10px; margin-bottom: 12px; }
  .info-icon { flex: none; width: 25px; height: 25px; border-radius: 50%; background: var(--gold); display: flex; align-items: center; justify-content: center; }
  .info-phone { font-family: "Poppins", sans-serif; font-weight: 600; font-size: 17px; color: var(--text-dark); }
  .info-text { font-family: "Tinos", serif; font-size: 10px; line-height: 1.45; color: var(--text-dark); }
</style>
</head>
<body>
<main class="sheet">

  <section class="card card--front" aria-label="Card front">
    <div class="front-mark"></div>
    <h1 class="front-name">Willowmere Counseling</h1>
    <div class="front-rule"></div>
    <p class="front-tagline">ENDURE - MEND - FLOURISH</p>
    <div class="front-dots"><span></span><span class="is-main"></span><span></span></div>
    <p class="front-web">www.<b>WillowmereCounseling</b>.example</p>
  </section>

  <section class="card card--back" aria-label="Card back">
    <svg class="back-panel" width="600" height="341" viewBox="0 0 600 341" aria-hidden="true">
      <path d="M242,0 C188,40 170,122 220,160 C262,192 300,224 302,252 C252,270 236,318 252,341 L600,341 L600,0 Z" fill="#ffffff"/>
    </svg>

    <div class="back-mark-row">
      <div class="back-mark"></div>
      <p class="back-name">Willowmere Counseling</p>
      <p class="back-tagline">ENDURE - MEND - FLOURISH</p>
    </div>

    <div class="info">
      <span class="info-pill">WILLOWMERE COUNSELING</span>
      <p class="info-tagline">ENDURE - MEND - FLOURISH</p>
      <ul class="info-list">
        <li class="info-item">
          <span class="info-icon">
            <svg width="13" height="13" viewBox="0 0 24 24"><path d="M6.6 10.8a15 15 0 0 0 6.6 6.6l2.2-2.2a1 1 0 0 1 1-.25 11.4 11.4 0 0 0 3.6.57 1 1 0 0 1 1 1V20a1 1 0 0 1-1 1A17 17 0 0 1 3 4a1 1 0 0 1 1-1h3.5a1 1 0 0 1 1 1c0 1.25.2 2.45.57 3.6a1 1 0 0 1-.25 1z" fill="#fff"/></svg>
          </span>
          <span class="info-phone">(214) 555-0187</span>
        </li>
        <li class="info-item">
          <span class="info-icon">
            <svg width="12" height="14" viewBox="0 0 24 28"><path d="M12 1a9 9 0 0 0-9 9c0 7 9 17 9 17s9-10 9-17a9 9 0 0 0-9-9zm0 12.5A3.5 3.5 0 1 1 12 6.5a3.5 3.5 0 0 1 0 7z" fill="#fff"/></svg>
          </span>
          <span class="info-text">3870 N. Garrick Ave., Suite 214, Fort Worth,<br>TX 76132</span>
        </li>
        <li class="info-item">
          <span class="info-icon">
            <svg width="14" height="14" viewBox="0 0 24 24" fill="none" stroke="#fff" stroke-width="1.6"><circle cx="12" cy="12" r="10"/><ellipse cx="12" cy="12" rx="4.5" ry="10"/><path d="M2 12h20M4 7h16M4 17h16"/></svg>
          </span>
          <span class="info-text">www.WillowmereCounseling.example</span>
        </li>
      </ul>
    </div>
  </section>

</main>
</body>
</html>
```